The Marisol & Jocelyn Fruit Co.

We produce a very high quality freeze dried fruit, all organic, no preservative, no additives, nothing but the fruit. To get more use out of a facility we have in Charlotte, we decided to pursue some high end online retailers with a high end freeze dried organic fruit. We are looking for a very high end, upper east side, trendy, hip, logo and package design for this. There are 4 SKU's - Freeze Dried Strawberries, Freeze Dried Blueberries, Freeze Dried Cherries, and a blend of of all 3 as the 4th SKU. 2 labels each that are 6" x 6" - The front, again needs to be fun and trendy big bold etc. Nothing frilly and Quiet Barn by the creek. The back needs to contain the nutritional statements for each and some copy describing the product and the company.
Updates
This would be one of only a few competitors in this segment
We are looking to steal a page from the wine industry. The coolest looking label on the shelf wins over the uneducated wine buyer. The designs are all fine, but they need to be sleeker, sexier, funner, etc. Someone should look at the label and say....wow that is FUN AND SEXY! I have to buy some! VORBEX.COM screams that. Don't worry so much about pictures of the fruit as the bag is going to be clear. Sell the brand not the fruit. OK?
Reason: Why not?
Reason: Final Selection by Monday 5pm EST.
For all designs that have not been eliminated:
Reason: Final selections. All four designs front and back on one file uploaded by noon tomorrow ( 12:01 PM EST New York)
Target Market(s)
People that would shop at sites like www.vorbex.com
Industry/Entity Type
It Company
Requirements
Nice to have
- The brand is named after our two daughters - One is very girly and the other is very "sassy" It would be fun to have the logo capture their personalities a little. I have uploaded a picture. Marisol on the left, Jocelyn on the right.
Also, another of our brands, Hank Pellow, packaging is attached here. Some consistency in look and feel may be good.
Should not have
- Nothing frilly or dainty, or delicate. Colorful fun and bold but trendy.

```html
<!DOCTYPE html>
<html lang="en">
<head>
<meta charset="utf-8">
<title>The Marisol &amp; Jocelyn Fruit Co. — Freeze Dried Cherries Label</title>
<link rel="stylesheet" href="https://fonts.googleapis.com/css2?family=Federo&family=Oswald:wght@300;400&display=swap">
<style>
  :root {
    --canvas: #f4f4f4;
    --paper: #ffffff;
    --ink: #1c1c1c;
    --cherry: #981b1e;
    --cherry-deep: #7a1417;
    --cherry-light: #c9585b;
    --rule: #3a3a3a;
  }
  html, body {
    margin: 0;
    padding: 0;
    width: 900px;
    height: 1200px;
    overflow: hidden;
    background: var(--canvas);
  }
  .canvas {
    position: relative;
    width: 900px;
    height: 1200px;
  }
  .label {
    position: absolute;
    left: 163px;
    top: 40px;
    width: 574px;
    height: 1120px;
    box-sizing: border-box;
    border: 2px solid var(--ink);
    background: var(--paper);
  }
  .label-panel {
    position: absolute;
    left: 36px;
    top: 36px;
    width: 498px;
    height: 1044px;
    border: 1px solid var(--ink);
    box-sizing: border-box;
    display: flex;
    flex-direction: column;
  }
  .pattern-band {
    width: 100%;
    background:
      linear-gradient(125deg,
        var(--cherry-deep) 0%,
        var(--cherry) 30%,
        var(--cherry-light) 50%,
        var(--cherry) 70%,
        var(--cherry-deep) 100%);
  }
  .pattern-band--top { height: 173px; }
  .pattern-band--bottom { height: 431px; }
  .brand-band {
    position: relative;
    height: 440px;
    background: var(--paper);
    text-align: center;
    color: var(--ink);
  }
  .wordmark {
    position: absolute;
    left: 0;
    right: 0;
    top: 62px;
    font-family: "Federo", "Poiret One", sans-serif;
    font-weight: 400;
    color: var(--ink);
    line-height: 1;
  }
  .wordmark span { display: block; }
  .wordmark-the { font-size: 17px; letter-spacing: 1px; margin-bottom: 4px; }
  .wordmark-name { font-size: 90px; letter-spacing: -2px; }
  .wordmark-and { font-size: 22px; margin: 2px 0 4px; }
  .wordmark-company { font-size: 15px; letter-spacing: 0.5px; margin-top: 6px; }
  .divider {
    position: absolute;
    left: 28px;
    right: 28px;
    top: 334px;
    border-top: 1px solid var(--rule);
  }
  .product-info {
    position: absolute;
    left: 0;
    right: 0;
    top: 350px;
    height: 80px;
    font-family: "Oswald", "Arial Narrow", sans-serif;
    font-weight: 300;
    font-size: 16px;
    line-height: 17px;
    color: var(--cherry);
    text-transform: uppercase;
  }
  .product-name {
    position: absolute;
    left: 58px;
    top: 14px;
    text-align: left;
    margin: 0;
  }
  .product-split {
    position: absolute;
    left: 246px;
    top: 0;
    height: 78px;
    border-left: 1px solid var(--rule);
  }
  .net-weight {
    position: absolute;
    right: 58px;
    top: 24px;
    text-align: center;
    margin: 0;
  }
  .net-weight .unit { text-transform: none; }
</style>
</head>
<body>
  <main class="canvas">
    <section class="label">
      <div class="label-panel">
        <div class="pattern-band pattern-band--top" role="img" aria-label="Decorative pattern of flowing cherry-red and white braided waves"></div>
        <div class="brand-band">
          <h1 class="wordmark">
            <span class="wordmark-the">THE</span>
            <span class="wordmark-name">MARISOL</span>
            <span class="wordmark-and">&amp;</span>
            <span class="wordmark-name">JOCELYN</span>
            <span class="wordmark-company">FRUIT COMPANY</span>
          </h1>
          <div class="divider"></div>
          <div class="product-info">
            <p class="product-name">Gourmet<br>Freeze Dried<br>Cherries</p>
            <div class="product-split"></div>
            <p class="net-weight">Net Weight<br>40 <span class="unit">oz</span>/140 <span class="unit">g</span></p>
          </div>
        </div>
        <div class="pattern-band pattern-band--bottom" role="img" aria-label="Decorative pattern of flowing cherry-red and white braided waves"></div>
      </div>
    </section>
  </main>
</body>
</html>
```